Brevanor Inc. Website

We need a website design for a new company based in Montreal, Canada. Our company offers professional services in planning & scheduling for major construction projects in varying industries. The main colors to be used are black & red (same as in logo). The final design should convey professionalism, precision, and excellence. The following are examples of what the website layout could look like: https://www.quilvardo.ca/, https://7496.ca/, https://lumavikt.ca/, https://www.dremorhext.com/en. Avoid using stock videos or photos with people in it.
Target audience are multi-national clients looking to hire a firm to manage their construction projects. Target market is Mining & Metals
Mining & Metalurgy, Hydroelectricity, Infrastructure
1 page

```html
<!DOCTYPE html>
<html lang="en">
<head>
<meta charset="utf-8">
<title>Brevanor Inc. | Planning &amp; Scheduling</title>
<link href="https://fonts.googleapis.com/css2?family=Roboto:wght@300;400;500;700;900&family=Jost:wght@300;400;500&display=swap" rel="stylesheet">
<style>
:root{
  --red:#a0081d;
  --red-deep:#9b0a1e;
  --ink:#111111;
  --dark:#222222;
  --black:#050505;
  --white:#ffffff;
  --line:#d9d9d9;
  --muted:#cfcfcf;
}
*{margin:0;padding:0;box-sizing:border-box}
html,body{width:1200px;height:4298px;overflow:hidden}
body{position:relative;background:var(--white);font-family:"Jost",sans-serif;color:var(--ink)}
.abs{position:absolute}

/* guide line */
.guide{left:75px;top:150px;width:1px;height:3764px;background:var(--line);z-index:3}
.guide-mark{left:74px;width:3px;z-index:4}
.index{left:68px;font-family:"Roboto",sans-serif;font-size:14px;z-index:4}

/* hero */
.hero{left:0;top:0;width:1135px;height:751px;border-bottom-right-radius:60px;overflow:hidden;
  background:linear-gradient(100deg,#5a4638 0%,#8a6a4c 30%,#c9b08a 55%,#2f5f9a 72%,#e8e6df 85%,#a98c67 100%)}
.hero-shade{inset:0;background:linear-gradient(90deg,rgba(0,0,0,.55),rgba(0,0,0,.15) 60%,rgba(0,0,0,0))}
.brand{left:62px;top:38px;font-family:"Roboto",sans-serif;font-weight:700;font-size:22px;color:var(--white);display:flex;align-items:center;gap:10px;z-index:5}
.brand i{width:16px;height:16px;border-radius:50%;background:var(--red);display:block}
.nav a{position:absolute;top:45px;font-family:"Jost",sans-serif;font-size:15px;color:var(--white);text-decoration:none;z-index:5}
.btn{display:flex;align-items:center;justify-content:center;border-radius:30px;font-family:"Roboto",sans-serif;font-weight:700;font-size:13px;letter-spacing:.3px;text-transform:uppercase;z-index:5}
.btn-red{background:var(--red);color:var(--white)}
.btn-white{background:var(--white);color:var(--red)}
.hero-title{left:163px;top:236px;font-family:"Roboto",sans-serif;font-size:56px;line-height:68px;color:var(--white);font-weight:300;z-index:5;text-transform:uppercase}
.hero-title strong{font-weight:900}

/* about */
.about{left:0;top:751px;width:1200px;height:1035px;background:var(--dark)}
.eyebrow{font-family:"Roboto",sans-serif;font-size:20px;letter-spacing:1.5px;text-transform:uppercase}
.big{font-family:"Roboto",sans-serif;font-size:52px;line-height:60px;text-transform:uppercase;font-weight:300}
.big strong{font-weight:900}
.about-copy{left:623px;top:866px;width:470px;color:var(--white);font-size:14.5px;line-height:26px;font-weight:300}
.about-copy p+p{margin-top:26px}
.photo{border-radius:8px}

/* services */
.card{width:305px;height:394px;border:1px solid #e6e6e6;border-radius:10px;overflow:hidden;background:var(--white);box-shadow:0 3px 8px rgba(0,0,0,.06)}
.card .pic{height:292px}
.card h3{font-family:"Roboto",sans-serif;font-weight:700;font-size:18.5px;padding:36px 0 0 30px;text-transform:uppercase}

/* projects */
.projects{left:0;top:3016px;width:1200px;height:898px;background:var(--red-deep)}
.caption{left:441px;top:3672px;width:415px;height:83px;background:var(--white);border-radius:8px;padding:14px 24px}
.caption h4{font-family:"Roboto",sans-serif;font-weight:500;font-size:22px;text-transform:uppercase}
.caption p{font-size:12px;margin-top:4px}

/* footer */
.footer{left:0;top:3914px;width:1200px;height:384px;background:var(--black)}
.foot-brand{left:0;top:4032px;width:1200px;text-align:center;font-family:"Roboto",sans-serif;font-weight:700;font-size:34px;color:var(--red)}
.social{top:4136px;width:30px;height:30px;border-radius:50%;background:var(--red)}
.rule{left:194px;width:811px;height:1px;background:#3a3a3a}
.foot-nav{top:4192px;font-family:"Roboto",sans-serif;font-size:15px;color:var(--white);text-transform:uppercase}
.copy{left:0;top:4256px;width:1200px;text-align:center;color:var(--white);font-size:14px}
</style>
</head>
<body>

<!-- hero -->
<section class="abs hero" role="img" aria-label="Hydroelectric powerhouse hall with blue and white generator units">
  <div class="abs hero-shade"></div>
</section>
<div class="abs brand"><i></i>Brevanor Inc.</div>
<nav class="nav">
  <a style="left:375px">Home</a>
  <a style="left:468px">About</a>
  <a style="left:561px">Services</a>
  <a style="left:668px">Projects</a>
  <a style="left:772px">Careers</a>
</nav>
<a class="abs btn btn-red" style="left:971px;top:38px;width:129px;height:37px">Contact Us</a>
<div class="abs index" style="top:236px;color:var(--white)">01</div>
<h1 class="abs hero-title">We’re here to<br><strong>Plan &amp; Shedule</strong><br>your projects</h1>
<a class="abs btn btn-red" style="left:162px;top:497px;width:235px;height:50px">Discover what we do</a>

<!-- about -->
<section class="abs about"></section>
<div class="guide abs"></div>
<div class="abs index" style="top:862px;color:var(--white)">02</div>
<div class="abs guide-mark" style="top:893px;height:220px;background:var(--white)"></div>
<div class="abs eyebrow" style="left:163px;top:860px;color:var(--white)">About us</div>
<h2 class="abs big" style="left:162px;top:901px;color:var(--white)"><strong>Making the</strong><br>difference</h2>
<a class="abs btn btn-red" style="left:162px;top:1053px;width:150px;height:44px">Learn more</a>
<div class="abs about-copy">
  <p>Lorem ipsum dolor sit amet, consectetur adipiscing elit, sed eiusmod tempor incididunt labore et dolore nisi magna aliqua. Ut enim ad minim veniam, quis nostrud exercitation ullamco laboris nisi ut aliquip commodo consequat.</p>
  <p>Duis aute irure dolor in reprehenderit in voluptate velit esse cillum dolore eu fugiat nulla pariatur. Excepteur sint occaecat cupidatat non proident, sunt in culpa officia deserunt mollit anim id est laborum.</p>
</div>
<div class="abs photo" role="img" aria-label="Black and white open-pit mine with stockpiles and stacker machine"
  style="left:162px;top:1182px;width:868px;height:480px;border-bottom-right-radius:50px;background:linear-gradient(135deg,#9a9a9a,#d0d0d0 45%,#6d6d6d 70%,#bdbdbd)"></div>
<div class="abs photo" role="img" aria-label="Steel structural frame against a blue sky"
  style="left:623px;top:1118px;width:512px;height:316px;border-radius:8px 8px 30px 8px;background:linear-gradient(160deg,#6c9fd6,#b9d4ef 45%,#8c8782 70%,#5c5854)"></div>

<!-- services -->
<div class="abs index" style="top:1894px;color:var(--red)">03</div>
<div class="abs guide-mark" style="top:1924px;height:221px;background:var(--red)"></div>
<div class="abs eyebrow" style="left:163px;top:1920px;color:var(--red)">Our offers</div>
<h2 class="abs big" style="left:162px;top:1963px;color:var(--ink)"><strong>Our</strong> services</h2>
<a class="abs btn btn-red" style="left:983px;top:1968px;width:152px;height:43px">Learn more</a>

<article class="abs card" style="left:164px;top:2086px"><div class="pic" role="img" aria-label="Architectural plans on a desk with a hard hat" style="background:linear-gradient(135deg,#d9cbb2,#f2eee6 50%,#e4c54a)"></div><h3>Project management</h3></article>
<article class="abs card" style="left:497px;top:2086px"><div class="pic" role="img" aria-label="Tablet showing a floor plan on site" style="background:linear-gradient(135deg,#c6e04a,#8a9a5a 50%,#3d4a5a)"></div><h3>Project controls</h3></article>
<article class="abs card" style="left:829px;top:2086px"><div class="pic" role="img" aria-label="Aerial view of timber house framing" style="background:linear-gradient(135deg,#c99a45,#e0b866 50%,#8c6a3a)"></div><h3>Construction</h3></article>
<article class="abs card" style="left:164px;top:2515px"><div class="pic" role="img" aria-label="Pen signing a contract document" style="background:linear-gradient(135deg,#3c3c3c,#dfe6ef 50%,#2b78c9)"></div><h3>Contract management</h3></article>
<article class="abs card" style="left:497px;top:2515px"><div class="pic" role="img" aria-label="Spiral staircase sculpture under a blue sky" style="background:linear-gradient(160deg,#7ea6d8,#c7d6e6 50%,#9a7a6a)"></div><h3>Procurement</h3></article>
<article class="abs card" style="left:829px;top:2515px"><div class="pic" role="img" aria-label="Aerial view of a water treatment plant" style="background:linear-gradient(135deg,#4a4a46,#7a8a5a 50%,#2e2e2c)"></div><h3>Water treatment</h3></article>

<!-- projects -->
<section class="abs projects"></section>
<div class="abs index" style="top:3149px;color:var(--white)">04</div>
<div class="abs eyebrow" style="left:163px;top:3146px;color:var(--white)">Recent work</div>
<h2 class="abs big" style="left:162px;top:3188px;color:var(--white)"><strong>Our</strong> projects</h2>
<a class="abs btn btn-white" style="left:983px;top:3193px;width:152px;height:43px">Learn more</a>
<div class="abs" role="img" aria-label="Tape measure lying on blueprints" style="left:164px;top:3316px;width:242px;height:453px;border-radius:0 0 0 90px;background:linear-gradient(150deg,#dce6f2,#aebfd6 50%,#3a3a3a)"></div>
<div class="abs" role="img" aria-label="Yellow tower crane beside a steel building frame" style="left:427px;top:3316px;width:443px;height:453px;border-radius:4px;background:linear-gradient(150deg,#c9ccd2,#8f959e 50%,#c8a030)"></div>
<div class="abs" role="img" aria-label="Concrete building under construction against a blue sky" style="left:891px;top:3316px;width:244px;height:453px;border-radius:0 110px 0 0;background:linear-gradient(160deg,#3d7bd0,#8fb3df 40%,#8a7f72)"></div>
<div class="abs caption"><h4>Rue Castelmont</h4><p>Lorem ipsum dolor sit amet, consectetur elit.</p></div>

<!-- footer -->
<footer class="abs footer"></footer>
<div class="abs foot-brand">Brevanor Inc.</div>
<div class="abs rule" style="top:4151px"></div>
<span class="abs social" style="left:516px"></span>
<span class="abs social" style="left:562px"></span>
<span class="abs social" style="left:609px"></span>
<span class="abs social" style="left:654px"></span>
<a class="abs foot-nav" style="left:220px">Home</a>
<span class="abs foot-nav" style="left:320px">I</span>
<a class="abs foot-nav" style="left:382px">About</a>
<span class="abs foot-nav" style="left:487px">I</span>
<a class="abs foot-nav" style="left:548px">Services</a>
<span class="abs foot-nav" style="left:669px">I</span>
<a class="abs foot-nav" style="left:729px">Projects</a>
<span class="abs foot-nav" style="left:854px">I</span>
<a class="abs foot-nav" style="left:915px">Careers</a>
<div class="abs rule" style="top:4239px"></div>
<div class="abs copy">Copyright © 2023 Brevanor Inc. All rights reserved.</div>

</body>
</html>
```